glow 482 is renewing its image

more dynamic website, make it look more attractive for the services we offer, at the same time more accurate on the services description. We want people to know we offer treatments that big corporations offer but not as expensive as they offer it. prices will be add by me once the website is approve

already have a website with wix.com www.glow482skin.com

Target Market(s)

women between 21 to 75

Industry/Entity Type

beauty services, body contouring

Colors

Designer to choose colors to be used in the design.

Requirements
Must have
• pictures of treatments
Nice to have
• accurate information about treatmnets, treatments menu
Should not have
• no online shopping

```html
<!DOCTYPE html>
<html lang="en">
<head>
<meta charset="utf-8">
<title>Glow 482 Skin Lounge</title>
<link href="https://fonts.googleapis.com/css2?family=Playfair+Display:wght@400;500;600&family=Poppins:ital,wght@0,400;0,500;1,400&display=swap" rel="stylesheet">
<style>
:root{
  --tan:#c8945e;
  --tan-dark:#a8713c;
  --cream:#f3eee8;
  --white:#ffffff;
  --ink:#1f1a16;
  --muted:#6b625a;
  --footer:#1d1a17;
  --leaf:#a9c0b8;
}
*{margin:0;padding:0;box-sizing:border-box}
html,body{width:1200px;height:4464px;overflow:hidden}
body{position:relative;background:var(--cream);font-family:'Poppins',sans-serif;color:var(--ink)}
.abs{position:absolute}
.serif{font-family:'Playfair Display',serif}

/* header */
.site-header{left:0;top:0;width:1200px;height:72px;background:var(--white)}
.brand{left:61px;top:8px;font-family:'Playfair Display',serif;font-size:44px;color:var(--tan);line-height:1}
.brand small{display:block;font-family:'Poppins',sans-serif;font-size:13px;margin:2px 0 0 44px;color:var(--tan)}
.nav{left:364px;top:29px;display:flex;gap:32px;font-size:12px;font-weight:500;text-transform:uppercase}
.nav a{color:var(--ink);text-decoration:none}
.nav a.active{color:var(--tan)}
.header-phone{left:992px;top:24px;display:flex;align-items:center;gap:10px;color:var(--tan);font-size:16px;font-style:italic}

/* hero */
.hero-panel{left:61px;top:75px;width:581px;height:525px;background:var(--tan)}
.hero-ghost{left:105px;top:150px;font-size:70px;color:rgba(255,255,255,.12);white-space:nowrap}
.hero-title{left:99px;top:235px;font-size:45px;line-height:1.18;color:var(--ink);font-weight:500}
.hero-text{left:99px;top:350px;width:440px;font-size:12px;line-height:22px;color:var(--white)}
.btn{display:flex;align-items:center;justify-content:center;font-size:13px;font-weight:500;text-transform:uppercase}
.btn-light{left:97px;top:444px;width:135px;height:36px;background:var(--white);color:var(--tan-dark)}
.hero-photo{left:642px;top:120px;width:497px;height:509px;background:linear-gradient(135deg,#d9d7d6,#efe3d7 55%,#c9b2a0)}

/* welcome */
.welcome{left:196px;top:678px;width:808px;height:291px;background:var(--white);text-align:center}
.welcome-ghost{left:0;top:60px;width:100%;font-size:64px;color:rgba(200,148,94,.15);white-space:nowrap}
.welcome h2{position:absolute;left:0;top:47px;width:100%;font-family:'Playfair Display',serif;font-weight:500;font-size:35px;line-height:42px}
.welcome p{position:absolute;left:112px;top:140px;width:584px;font-size:12.5px;font-style:italic;line-height:19.5px;color:var(--muted)}

.section-title{left:0;top:1030px;width:1200px;text-align:center;font-size:35px;font-weight:500}

/* treatment cards */
.t-frame{border:2px solid var(--tan)}
.t-photo{border:1px solid rgba(0,0,0,.05)}
.t-card{background:var(--white);padding:38px 60px 0 62px}
.t-card .mark{font-family:'Playfair Display',serif;font-size:32px;color:var(--tan);line-height:1}
.t-card h3{font-family:'Playfair Display',serif;font-weight:500;font-size:22px;line-height:29px;margin-top:12px}
.t-card p{font-size:12px;line-height:19.5px;color:var(--muted);margin-top:18px}
.t-card .btn{width:135px;height:36px;background:var(--tan);color:var(--white);margin-top:20px}
.leaves{background:radial-gradient(ellipse at center,var(--leaf) 0%,rgba(169,192,184,.35) 55%,rgba(169,192,184,0) 75%)}

.dots{left:578px;top:3230px;display:flex;gap:6px;align-items:center}
.dots span{width:7px;height:7px;border-radius:50%;background:var(--tan)}
.dots span.on{width:13px;height:13px;background:none;border:2px solid var(--tan);position:relative}

/* subscribe */
.subscribe{left:0;top:3315px;width:1200px;height:373px;background:linear-gradient(90deg,#b27c46 0%,#c9a079 45%,#d8c1a4 70%,#cdb595 100%)}
.sub-kicker{left:61px;top:3383px;font-family:'Playfair Display',serif;font-style:italic;font-size:19px;color:var(--white)}
.sub-title{left:61px;top:3410px;width:560px;font-size:33px;line-height:40px;color:var(--white);font-weight:500}
.field{left:61px;width:294px;height:35px;border:1px solid rgba(255,255,255,.8);color:var(--white);font-size:11px;padding:10px 10px}
.btn-sub{left:61px;top:3591px;width:133px;height:34px;background:var(--tan);color:var(--white)}

/* promo */
.promo-back{background:var(--white);box-shadow:0 2px 12px rgba(0,0,0,.05)}
.promo-label{font-family:'Playfair Display',serif;font-size:22px;text-align:center;font-weight:500}
.promo-dark{background:linear-gradient(135deg,#3b3a38,#5a5651 60%,#7b8a6f)}
.promo-dark h4{position:absolute;left:46px;top:100px;font-family:'Playfair Display',serif;font-weight:500;color:var(--white);font-size:22px;line-height:30px}

/* footer */
.site-footer{left:0;top:4136px;width:1200px;height:294px;background:var(--footer)}
.f-brand{left:61px;top:4208px;font-family:'Playfair Display',serif;font-size:46px;color:var(--tan);line-height:1}
.f-brand small{display:block;font-family:'Poppins',sans-serif;font-size:13px;margin:2px 0 0 46px}
.social{top:4290px;width:32px;height:32px;border-radius:50%;background:var(--white)}
.f-col h5{font-family:'Playfair Display',serif;font-weight:500;font-size:18px;color:var(--tan);margin-bottom:14px}
.f-col li{list-style:none;font-size:11px;color:#d6d0ca;line-height:27px}
.f-contact{display:flex;gap:16px;font-size:11px;line-height:20px;color:#e0dad3;margin-bottom:16px}
.f-contact svg{flex:none;margin-top:3px}
.f-policy a{color:#e0dad3;font-size:11px;line-height:19px;text-decoration:underline;display:block}
.f-policy p{color:#d6d0ca;font-size:11px;line-height:19px;margin-top:12px;width:230px}
.bottom-bar{left:0;top:4430px;width:1200px;height:34px;background:var(--tan);color:var(--white);font-size:11px;text-align:center;line-height:34px}
</style>
</head>
<body>

<header class="abs site-header">
  <div class="abs brand">Glow 482<small>Skin Lounge</small></div>
  <nav class="abs nav">
    <a class="active" href="#">Home</a><a href="#">Treatments</a><a href="#">Best Surgery Treatment</a><a href="#">Contact Us</a><a href="#">About Us</a><a href="#">More</a>
  </nav>
  <div class="abs header-phone">
    <svg width="20" height="20" viewBox="0 0 24 24"><path fill="#a8713c" d="M6.6 10.8a15.1 15.1 0 0 0 6.6 6.6l2.2-2.2c.3-.3.7-.4 1-.2 1.1.4 2.3.6 3.6.6.6 0 1 .4 1 1V20c0 .6-.4 1-1 1A17 17 0 0 1 3 4c0-.6.4-1 1-1h3.5c.6 0 1 .4 1 1 0 1.3.2 2.5.6 3.6.1.3 0 .7-.2 1z"/></svg>
    (555) 014-2290
  </div>
</header>

<section>
  <div class="abs hero-panel"></div>
  <div class="abs hero-ghost serif">Glow 482</div>
  <h1 class="abs hero-title serif">Skin Lounge and Post<br>Liposuction Care</h1>
  <p class="abs hero-text">Located in Springvale, CT. Glow 482 Skin Lounge makes the most of what you've got with services designed to complement your looks and needs.</p>
  <a class="abs btn btn-light">Learn More</a>
  <div class="abs hero-photo" role="img" aria-label="Photo of a woman receiving a microdermabrasion facial treatment"></div>
</section>

<section class="abs welcome">
  <div class="abs welcome-ghost serif">Welcome Glow 482</div>
  <h2>Skin Lounge and Post<br>Liposuction Care</h2>
  <p>Located in Springvale, CT. Glow 482 Skin Lounge makes the most of what you've got with services designed to complement your looks and needs. We feature an extensive list of treatments, including natural peels, tripolar radio frequency, microdermabrasion, facial and body microcurrent, post operatory Treatment, wood therapy, ultrasound body sculpting, complete facial treatment packages, vacuum therapy and much more!</p>
</section>

<h2 class="abs section-title serif">Our Treatments</h2>

<!-- treatment 1 -->
<div class="abs t-frame" style="left:203px;top:1113px;width:434px;height:464px"></div>
<div class="abs t-photo" role="img" aria-label="Photo of a woman with a facial mask receiving a peel treatment" style="left:192px;top:1103px;width:437px;height:466px;background:linear-gradient(135deg,#8a5a3c,#d9b9a0 50%,#efe4d8)"></div>
<div class="abs t-card" style="left:482px;top:1163px;width:413px;height:328px">
  <div class="mark">Glow 482</div>
  <h3>Maximum Glow 482<br>Natural Peel</h3>
  <p>NON-ACID, herbal formula that is more effective than traditional acids and that is equivalent to 15 microdermoabrasions without the use of acids or harmful crystals.</p>
  <a class="btn">Please Call</a>
</div>
<div class="abs leaves" role="img" aria-label="Decorative green leaf sprig" style="left:895px;top:1222px;width:107px;height:217px"></div>

<!-- treatment 2 -->
<div class="abs t-frame" style="left:541px;top:1635px;width:433px;height:468px"></div>
<div class="abs t-photo" role="img" aria-label="Photo of a woman receiving an ultrasound post-surgery treatment" style="left:531px;top:1644px;width:435px;height:465px;background:linear-gradient(135deg,#e8e6e4,#cfc9c5 55%,#9f8c80)"></div>
<div class="abs t-card" style="left:227px;top:1705px;width:411px;height:327px">
  <div class="mark">Glow 482</div>
  <h3>Post-surgery Treatment</h3>
  <p>Glow 482 Skin Lounge After Lipo Massage is a specialized center in post liposuction massage (Tummy Tuck, Mammoplasty, Neck Lift, Breast Implant) using a combination of Lymphatic Drainage Massage, Ultrasound Massage, Ultrasound Cavitation, Vacuum Therapy.</p>
  <a class="btn">Please Call</a>
</div>
<div class="abs leaves" role="img" aria-label="Decorative green leaf sprig" style="left:127px;top:1769px;width:100px;height:208px"></div>

<!-- treatment 3 -->
<div class="abs t-frame" style="left:203px;top:2186px;width:434px;height:464px"></div>
<div class="abs t-photo" role="img" aria-label="Photo of an ultrasound cavitation device used on the body" style="left:192px;top:2176px;width:437px;height:466px;background:linear-gradient(135deg,#1e1e1e,#8c8a88 45%,#d9cfc4)"></div>
<div class="abs t-card" style="left:482px;top:2236px;width:413px;height:328px">
  <div class="mark">Glow 482</div>
  <h3>Ultrasound Cavitation</h3>
  <p>Body sculpting treatment with no anesthesia, no scars, no discomfort, no down-time and presents a risk-free alternative to liposuction.</p>
  <a class="btn">Please Call</a>
</div>
<div class="abs leaves" role="img" aria-label="Decorative green leaf sprig" style="left:895px;top:2295px;width:107px;height:217px"></div>

<!-- treatment 4 -->
<div class="abs t-frame" style="left:541px;top:2725px;width:433px;height:468px"></div>
<div class="abs t-photo" role="img" aria-label="Photo of a lipo-laser device being applied to the skin" style="left:531px;top:2733px;width:435px;height:463px;background:linear-gradient(135deg,#121212,#5a4a42 45%,#e0c3b0)"></div>
<div class="abs t-card" style="left:227px;top:2793px;width:411px;height:328px">
  <div class="mark">Glow 482</div>
  <h3>Lipo-Laser</h3>
  <p>Lipo-Laser is a non-surgical cold laser procedure that uses low level, laser-based light to reduce the stubborn, subcutaneous fat on targeted areas of your body.</p>
  <a class="btn">Please Call</a>
</div>
<div class="abs leaves" role="img" aria-label="Decorative green leaf sprig" style="left:106px;top:2855px;width:120px;height:208px"></div>

<div class="abs dots"><span></span><span class="on"></span><span></span></div>

<!-- subscribe -->
<section class="abs subscribe" role="img" aria-label="Background photo of spa massage tools and wooden rollers on a table"></section>
<div class="abs sub-kicker">Exclusive deals and discounts.</div>
<h2 class="abs sub-title serif">Get 10% off your first treatment when you subscribe!</h2>
<div class="abs field" style="top:3495px">Name :</div>
<div class="abs field" style="top:3541px">Email :</div>
<a class="abs btn btn-sub">Please Call</a>

<!-- promos -->
<div class="abs promo-back" style="left:234px;top:3806px;width:338px;height:260px"></div>
<div class="abs" role="img" aria-label="Photo of a woman receiving a facial treatment" style="left:189px;top:3757px;width:350px;height:269px;background:linear-gradient(135deg,#7a4a30,#d7b49a 55%,#efe2d6)"></div>
<div class="abs promo-label" style="left:234px;top:4030px;width:338px">Post Surgery Treatment</div>

<div class="abs promo-back" style="left:661px;top:3806px;width:339px;height:260px"></div>
<div class="abs promo-dark" role="img" aria-label="Photo of natural skincare products on a dark stone surface" style="left:616px;top:3757px;width:350px;height:269px">
  <h4>Complete Body and Facial<br>Treatments with 100%<br>Natural Products</h4>
</div>
<div class="abs promo-label" style="left:661px;top:4030px;width:339px">Natural Products</div>

<!-- footer -->
<footer class="abs site-footer"></footer>
<div class="abs f-brand">Glow 482<small>Skin Lounge</small></div>
<div class="abs social" style="left:61px" aria-label="Social link"></div>
<div class="abs social" style="left:106px" aria-label="Social link"></div>

<div class="abs f-col" style="left:338px;top:4204px">
  <h5>Sitemap</h5>
  <ul><li>- Home</li><li>- Treatments</li><li>- Post Surgery Treatment</li><li>- Contact Us</li><li>- About Us</li></ul>
</div>

<div class="abs f-col" style="left:612px;top:4204px">
  <h5>Contact Us</h5>
  <div class="f-contact">
    <svg width="22" height="22" viewBox="0 0 24 24"><path fill="none" stroke="#c8945e" stroke-width="1.6" d="M12 22s7-7 7-12a7 7 0 0 0-14 0c0 5 7 12 7 12z"/><circle cx="12" cy="10" r="2.5" fill="none" stroke="#c8945e" stroke-width="1.6"/></svg>
    <div>18 Alder Court Springvale<br>CT 06100</div>
  </div>
  <div class="f-contact">
    <svg width="22" height="22" viewBox="0 0 24 24"><rect x="3" y="5" width="18" height="14" fill="none" stroke="#c8945e" stroke-width="1.6"/><path d="M3 6l9 7 9-7" fill="none" stroke="#c8945e" stroke-width="1.6"/></svg>
    <div>glow482spa@example.com</div>
  </div>
  <div class="f-contact">
    <svg width="22" height="22" viewBox="0 0 24 24"><path fill="none" stroke="#c8945e" stroke-width="1.6" d="M6.6 10.8a15.1 15.1 0 0 0 6.6 6.6l2.2-2.2c.3-.3.7-.4 1-.2 1.1.4 2.3.6 3.6.6.6 0 1 .4 1 1V20c0 .6-.4 1-1 1A17 17 0 0 1 3 4c0-.6.4-1 1-1h3.5c.6 0 1 .4 1 1 0 1.3.2 2.5.6 3.6.1.3 0 .7-.2 1z"/></svg>
    <div>(555) 014-2290 or<br>(555) 014-7731</div>
  </div>
</div>

<div class="abs f-col f-policy" style="left:888px;top:4204px">
  <h5>Policy</h5>
  <a href="#">Reservation Fee and<br>Cancellation Policy</a>
  <p>To schedule your appointment have your DealPass voucher # ready to secure your date and time.</p>
</div>

<div class="abs bottom-bar">© 2021 Glow 482 Skin Lounge- All Right Reserved.</div>

</body>
</html>
```